Personal Business Card

Looking for a clean and modern personal business card. Basically I need something catchy to give to potential clients and people I meet. I do a lot of freelancing (from DJ'ing to wedding videography, but its mostly on the event side of things) so it's more-so about selling myself rather than identifying with a company. I'm starting to meet more people that I want to work with after meeting them so I'm revamping my business cards.

I'm looking for a clean and modern design- I know that's really vague but I'm fine with anything ranging from a symbol to just a fancy version of my name.

Details I need on the front:
Dennis Kowal
dennis@denniskowal-mail.net
(555) 807-2291

On the back I'd like to have something simple like "Nice to have met you today" or "Great meeting you".

UPDATE 9/27 Noon: My apologies for not putting it up before- I'm definitely looking for full color. Doesn't have to be a rainbow but I am looking for the least amount of blank white as possible.

UPDATE 10/1: Really impressed with what I've been getting so far and I'm working on giving everyone feedback- if your design is still up then you're still in the run. Looking for something more unique and modern so please do not post something that looks like a template from Cardloom!

Target Market(s)

Mainly to give to people aged 18-35. Most of my encounters will be casual so the card should have a "young" feeling to it. I rarely do anything in the corporate world so it doesn't have to be boring. It should give the impression that I'm the one they should go to if they need what I do (again it changes every weekend so I'll probably say the "what I do" part.

Industry/Entity Type

Wedding

Requirements
Must have
• Basically the contact information listed above
Nice to have
• I really like the colors Blue, Silver, and Purple. They don't have to necessarily all be there though. I do like the look of polished metal if that makes sense.
Should not have
• A template that resembles card-loom. I'm in a point in my life where I'm working a lot of different markets/areas so the card does not need to have an address or address placeholder.

```html
<!DOCTYPE html>
<html lang="en">
<head>
<meta charset="utf-8">
<title>Dennis Kowal – Business Card</title>
<link rel="stylesheet" href="https://fonts.googleapis.com/css2?family=Montserrat:wght@300;400;500&display=swap">
<style>
  :root {
    --page: #ffffff;
    --card-bg: #dcdcdc;
    --teal: #2fb3bd;
    --charcoal: #323636;
    --coral: #d9573f;
    --berry: #b63a55;
    --ink: #373a3a;
  }
  * { margin: 0; padding: 0; box-sizing: border-box; }
  html, body {
    width: 1200px; height: 1000px; overflow: hidden;
    background: var(--page);
    font-family: "Montserrat", sans-serif;
  }
  .card {
    position: absolute; left: 38px; top: 163px;
    width: 1125px; height: 675px;
    background: radial-gradient(circle at 70% 40%, #e2e2e2, var(--card-bg));
    overflow: hidden;
  }
  .card-artwork { position: absolute; inset: 0; width: 100%; height: 100%; }
  .wordmark {
    position: absolute; left: 535px; top: 140px; width: 500px;
    text-align: center; color: var(--teal);
    font-size: 44px; font-weight: 500; letter-spacing: 1px;
  }
  .holder-name {
    position: absolute; left: 535px; top: 357px;
    font-size: 62px; line-height: 1; color: var(--ink); white-space: nowrap;
  }
  .holder-name .first { font-weight: 300; }
  .holder-name .last { font-weight: 500; }
  .contact-row {
    position: absolute; left: 550px;
    display: flex; align-items: center; gap: 14px;
    font-size: 28px; font-weight: 400; color: var(--ink);
  }
  .contact-row.phone { top: 452px; }
  .contact-row.email { top: 530px; }
  .contact-icon { width: 56px; height: 56px; flex: none; }
</style>
</head>
<body>
  <section class="card">
    <svg class="card-artwork" viewBox="0 0 1125 675" role="img" aria-label="Layered paper panel artwork in teal, charcoal, coral and berry tones">
      <defs>
        <linearGradient id="panel-blend" x1="0" y1="0" x2="1" y2="0.6">
          <stop offset="0" stop-color="var(--teal)"/>
          <stop offset="0.35" stop-color="var(--charcoal)"/>
          <stop offset="0.65" stop-color="var(--coral)"/>
          <stop offset="1" stop-color="var(--berry)"/>
        </linearGradient>
      </defs>
      <path d="M0,0 L290,0 Q380,420 752,675 L0,675 Z" fill="url(#panel-blend)"/>
    </svg>

    <div class="wordmark">Dennis Kowal</div>

    <h1 class="holder-name"><span class="first">Dennis</span> <span class="last">Kowal</span></h1>

    <div class="contact-row phone">
      <svg class="contact-icon" viewBox="0 0 56 56" aria-hidden="true">
        <circle cx="28" cy="28" r="25" fill="none" stroke="var(--ink)" stroke-width="3"/>
        <path d="M21,15 C18,16 17,19 17,22 C18,31 25,38 34,39 C37,39 40,38 41,35 L36,31 L32,33 C28,31 25,28 23,24 L25,20 Z" fill="var(--ink)"/>
      </svg>
      <span>(555) 807-2291</span>
    </div>

    <div class="contact-row email">
      <svg class="contact-icon" viewBox="0 0 56 56" aria-hidden="true">
        <circle cx="28" cy="28" r="25" fill="none" stroke="var(--ink)" stroke-width="3"/>
        <g fill="none" stroke="var(--ink)" stroke-width="2.2">
          <circle cx="28" cy="28" r="14"/>
          <ellipse cx="28" cy="28" rx="6" ry="14"/>
          <line x1="14" y1="28" x2="42" y2="28"/>
          <line x1="16" y1="21" x2="40" y2="21"/>
          <line x1="16" y1="35" x2="40" y2="35"/>
        </g>
      </svg>
      <span>dennis@denniskowal-mail.net</span>
    </div>
  </section>
</body>
</html>
```